eBook Design & Mockup for my Compass Toward Grand Diamond Success & Joy!

I'm an entrepreneur looking for design help for an eBook I'm offering to sports parents. This is a project that will impact a ton of families in sports! My target audience is a Sports Mom or Dad raising a 6th to 12th Grade baseball student-athlete. This particular contest is for a softcover book mockup for an eBook I'm producing. More specific details can be found in the attached file. Additionally, the link to my Google Doc explaining the project can be found below.

```html
<!DOCTYPE html>
<html lang="en">
<head>
<meta charset="utf-8">
<title>Compass Toward Grand Diamond Success &amp; Joy — eBook Cover</title>
<link rel="stylesheet" href="https://fonts.googleapis.com/css2?family=Barlow+Semi+Condensed:wght@600;700;800&family=Roboto:wght@400;500&family=Roboto+Condensed:wght@700&display=swap">
<style>
  :root {
    --page-bg: #ffffff;
    --title-white: #ffffff;
    --title-blue: #3fbdf1;
    --title-yellow: #fff21c;
    --stamp-red: #d4212a;
    --band-bg: rgba(40, 36, 44, 0.55);
    --sky-top: #2e2a33;
    --sky-mid: #5a4a4a;
    --sky-glow: #b9733f;
    --stands: #17181c;
    --field-dark: #2d5a22;
    --field-light: #4f8a34;
  }
  * { margin: 0; padding: 0; box-sizing: border-box; }
  html, body {
    width: 1200px;
    height: 1055px;
    overflow: hidden;
    background: var(--page-bg);
  }
  .book-cover {
    position: absolute;
    left: 270px;
    top: 67px;
    width: 660px;
    height: 920px;
    overflow: hidden;
    box-shadow: 0 6px 24px rgba(0, 0, 0, 0.25);
  }
  .stadium-scene {
    position: absolute;
    inset: 0;
    background:
      radial-gradient(ellipse 60% 18% at 50% 78%, rgba(154, 90, 58, 0.55), transparent 70%),
      linear-gradient(180deg,
        var(--sky-top) 0%,
        var(--sky-mid) 30%,
        var(--sky-glow) 48%,
        #4a3a35 58%,
        var(--stands) 62%,
        var(--stands) 76%,
        var(--field-dark) 79%,
        var(--field-light) 90%,
        var(--field-dark) 100%);
  }
  .title-block {
    position: absolute;
    left: 72px;
    top: 58px;
    width: 520px;
    font-family: "Barlow Semi Condensed", "Arial Narrow", sans-serif;
    font-weight: 800;
    text-transform: uppercase;
    line-height: 0.9;
    letter-spacing: 0.5px;
  }
  .title-lead { color: var(--title-white); font-size: 60px; }
  .title-compass { color: var(--title-blue); font-size: 100px; }
  .title-row { display: flex; align-items: center; gap: 10px; }
  .title-stack {
    display: flex;
    flex-direction: column;
    color: var(--title-white);
    font-size: 40px;
    line-height: 0.92;
  }
  .title-big-yellow { color: var(--title-yellow); font-size: 96px; }
  .stamp {
    position: absolute;
    left: 34px;
    top: 52px;
    padding: 2px 10px;
    border: 3px solid var(--stamp-red);
    color: var(--stamp-red);
    font-family: "Roboto Condensed", "Arial Narrow", sans-serif;
    font-weight: 700;
    font-size: 30px;
    letter-spacing: 2px;
    transform: rotate(-17deg);
    transform-origin: left top;
  }
  .subtitle-band {
    position: absolute;
    left: 0;
    top: 470px;
    width: 100%;
    height: 132px;
    background: var(--band-bg);
    display: flex;
    align-items: center;
    justify-content: center;
    padding: 0 40px;
  }
  .subtitle {
    font-family: "Roboto", Arial, sans-serif;
    font-weight: 400;
    font-size: 28px;
    line-height: 1.22;
    color: var(--title-white);
    text-align: center;
  }
  .author {
    position: absolute;
    left: 0;
    bottom: 30px;
    width: 100%;
    text-align: center;
    font-family: "Roboto", Arial, sans-serif;
    font-weight: 500;
    font-size: 27px;
    letter-spacing: 1px;
    color: var(--title-white);
  }
</style>
</head>
<body>
  <div class="book-cover">
    <div class="stadium-scene" role="img" aria-label="Photograph of a baseball stadium at dusk with glowing sky, lit stands and a green diamond field"></div>

    <div class="title-block">
      <div class="title-lead">Your Athlete’s</div>
      <div class="title-compass">Compass</div>
      <div class="title-row">
        <div class="title-stack"><span>Toward</span><span>Grand</span></div>
        <span class="title-big-yellow">Diamond</span>
      </div>
      <div class="title-row">
        <span class="title-big-yellow">Success</span>
        <div class="title-stack"><span>(And</span><span>Joy)</span></div>
      </div>
    </div>

    <div class="stamp">INTERVIEW</div>

    <div class="subtitle-band">
      <p class="subtitle">29 Lessons Every Family Should Learn About Guiding a Young Player Toward Growth in the Game and Beyond</p>
    </div>

    <div class="author">MARCUS “M.T.” DOYLE</div>
  </div>
</body>
</html>
```